Update Law Firm Website

Update law firm website pages, add pages for employees. Current website looks stale. www.vantholmlegal.example

Target Market(s)

Personal injury clients

Industry/Entity Type

Legal

Number of Pages Required

5+ page

Font styles to use
Serif

Requirements
Must have
• User friendly and engaging design
Nice to have
• ?
Should not have
• scales of justice, law books,

```html
<!DOCTYPE html>
<html lang="en">
<head>
<meta charset="utf-8">
<title>Vantholm Injury Law Group</title>
<link href="https://fonts.googleapis.com/css2?family=Libre+Baskerville:wght@400;700&family=Open+Sans:wght@400;600;700&display=swap" rel="stylesheet">
<style>
:root{
  --gold:#fbc965;
  --gold-deep:#e9ad3b;
  --gold-text:#f7c65f;
  --dark:#2e2e2e;
  --ink:#333;
  --muted:#666;
  --cream:#fdf3e5;
  --white:#fff;
  --serif:"Libre Baskerville", Georgia, serif;
  --sans:"Open Sans", Arial, sans-serif;
}
*{box-sizing:border-box;margin:0;padding:0}
html,body{width:1200px;height:3125px;overflow:hidden}
body{position:relative;font-family:var(--sans);color:var(--ink);background:var(--white)}
.abs{position:absolute}
.btn{position:absolute;display:flex;align-items:center;justify-content:center;border-radius:8px;font-size:20px;text-transform:uppercase;letter-spacing:.5px}
.btn-gold{background:var(--gold);color:#3a2e12}
.btn-dark{background:var(--dark);color:var(--white)}
.accent{position:absolute;height:4px;width:58px;background:var(--gold-deep)}
.section-title{position:absolute;font-family:var(--serif);font-weight:400;font-size:32px;color:#222;white-space:nowrap}
.copy{position:absolute;font-size:16px;line-height:21px;color:var(--muted)}

/* top bar */
.topbar{left:0;top:0;width:1200px;height:52px;background:var(--dark);color:#eee;font-size:15px}
.topbar .item{position:absolute;top:0;height:52px;display:flex;align-items:center;gap:8px;white-space:nowrap}
.appointment{position:absolute;left:862px;top:0;width:259px;height:52px;background:var(--gold);color:#2b2b2b;font-size:19px;display:flex;align-items:center;justify-content:center}

/* nav */
.nav{left:0;top:52px;width:1200px;height:73px;background:var(--white)}
.brand{position:absolute;left:79px;top:10px;text-align:center}
.brand .name{font-family:var(--serif);font-weight:700;font-size:21px;color:#222;letter-spacing:.3px}
.brand .sub{font-family:var(--serif);font-size:13px;color:var(--gold-deep);margin-top:3px}
.menu a{position:absolute;top:13px;height:46px;display:flex;align-items:center;font-size:17px;color:#222;text-decoration:none}
.menu a.active{background:var(--gold);border-radius:8px;padding:0 20px}

/* hero */
.hero{left:0;top:125px;width:1200px;height:573px;background:radial-gradient(ellipse at 30% 40%,#c78b62 0%,#8a5138 45%,#3c2219 100%)}
.hero-title{position:absolute;right:79px;top:238px;font-size:54px;font-weight:700;color:var(--gold-text);letter-spacing:-.5px}
.hero-with{position:absolute;right:79px;top:310px;font-family:var(--serif);font-size:26px;color:var(--gold-text)}
.hero-with b{font-size:30px}
.hero-text{position:absolute;right:79px;top:356px;width:760px;text-align:right;font-size:25px;line-height:34px;color:var(--white)}

/* services */
.service{position:absolute;font-size:21px;color:#222}
.service svg{display:block;margin-bottom:14px}

/* about */
.about{left:0;top:1079px;width:1200px;height:442px;background:var(--cream);overflow:hidden}
.about-photo{position:absolute;left:79px;top:111px;width:366px;height:248px;border:7px solid var(--white);box-shadow:0 2px 8px rgba(0,0,0,.15);background:linear-gradient(135deg,#e6e6e6,#9a9a9a 60%,#4a4a4a)}

/* consult band */
.consult{left:0;top:1521px;width:1200px;height:135px;background:linear-gradient(90deg,#e8b04a,#f5cf7a 40%,#e3ad48)}
.consult-title{position:absolute;left:82px;top:22px;font-family:var(--serif);font-size:36px;line-height:46px;color:#2a2a2a;text-align:center}

/* news */
.card-img{position:absolute;width:311px;height:153px;background:linear-gradient(135deg,#e9e9e9,#b8b8b8 55%,#6e6e6e)}
.date{position:absolute;height:38px;width:86px;background:var(--gold);border-radius:0 0 14px 0;font-size:24px;display:flex;align-items:center;justify-content:center;color:#222}
.date small{font-size:14px;margin-left:4px}
.card-title{position:absolute;font-family:var(--serif);font-weight:400;font-size:18px;color:#222;white-space:nowrap}
.card-meta{position:absolute;font-size:13px;color:#555;display:flex;gap:14px;width:311px}
.card-text{position:absolute;width:311px;font-size:16px;line-height:21px;color:var(--muted)}
.read-more{position:absolute;font-size:14px;color:var(--gold-deep);text-decoration:underline;display:flex;align-items:center;gap:6px}

/* callback */
.callback{left:0;top:2062px;width:1200px;height:292px;background:var(--gold)}
.field{position:absolute;left:79px;width:323px;border-bottom:2px solid #8a6a2a;font-size:14px;color:#7a5c20;padding-bottom:8px}
.message{position:absolute;left:421px;top:65px;width:325px;height:115px;border:2px solid #8a6a2a;font-size:14px;color:#7a5c20;padding:10px}

/* testimonials */
.quote{position:absolute;width:320px}
.quote .text{position:relative;font-size:16px;line-height:21px;color:#444;margin-top:6px}
.quote .avatar{position:absolute;left:0;top:158px;width:83px;height:84px;background:linear-gradient(180deg,#d9b8a6,#9a3b3b);border:3px solid #f2f2f2;box-shadow:0 1px 4px rgba(0,0,0,.2)}
.quote .who{position:absolute;left:98px;top:164px;font-family:var(--serif);font-size:17px;color:#222}
.quote .role{position:absolute;left:98px;top:194px;font-family:var(--serif);font-size:13px;color:#444}

/* footer */
.footer{left:0;top:2740px;width:1200px;height:385px;background:#2b2b2b;color:#ddd}
.footer h4{position:absolute;font-family:var(--serif);font-weight:400;font-size:18px;color:#eee}
.footer .links{position:absolute;left:525px;top:97px;list-style:none;font-size:16px;line-height:23px}
.contact-row{position:absolute;left:812px;display:flex;gap:14px;font-size:16px;line-height:22px}
.copyright{position:absolute;left:0;top:350px;width:1200px;text-align:center;font-size:15px;color:#eee}
.copyright b{font-weight:700}
.copyright span{color:var(--gold)}
</style>
</head>
<body>

<header class="abs topbar">
  <div class="item" style="left:79px">
    <svg width="18" height="13" viewBox="0 0 18 13"><rect width="18" height="13" rx="1" fill="#f2b84b"/><path d="M1 1l8 6 8-6" stroke="#2e2e2e" stroke-width="1.6" fill="none"/></svg>
    martin@vantholmlegal.example
  </div>
  <div class="item" style="left:360px">
    <svg width="16" height="16" viewBox="0 0 16 16"><path d="M3 1l3 3-2 2c1 2 3 4 5 5l2-2 3 3-2 3C7 15 1 9 1 3z" fill="#fff"/></svg>
    (555) 010-4477
  </div>
  <div class="item" style="left:535px">
    <svg width="16" height="16" viewBox="0 0 16 16"><circle cx="8" cy="8" r="7" fill="none" stroke="#f2b84b" stroke-width="2"/><path d="M8 4v4l3 2" stroke="#f2b84b" stroke-width="2" fill="none"/></svg>
    Mon - Sat(10am to 7pm)
  </div>
  <a class="appointment">MAKE AN APPOINTMENT</a>
</header>

<nav class="abs nav">
  <div class="brand">
    <div class="name">VANTHOLM INJURY LAW GROUP</div>
    <div class="sub">MARTIN K. VANTHOLM, ESQUIRE</div>
  </div>
  <div class="menu">
    <a class="active" style="left:590px">Home</a>
    <a style="left:704px">Services</a>
    <a style="left:812px">Results</a>
    <a style="left:917px">About Us</a>
    <a style="left:1035px">Contact Us</a>
  </div>
</nav>

<section class="abs hero" role="img" aria-label="Warm-toned photograph of a courtroom interior with wooden benches">
  <h1 class="hero-title">THE BEST LAW FIRM</h1>
  <div class="hero-with">With <b>MARTIN K. VANTHOLM</b>, ESQUIRE</div>
  <p class="hero-text">We Take all cases on a contingency basis,meaning you will not pay attorney fees or costs unless we recover on your behalf.</p>
</section>

<section class="services">
  <div class="accent" style="left:79px;top:744px"></div>
  <h2 class="section-title" style="left:79px;top:752px">Our Services</h2>
  <p class="copy" style="left:79px;top:812px;width:320px">Mr. Vantholm's success is based on his experience as an insurance defense attorney and Judge Pro Tem has provided him with the expertise, legal knowledge and persuasive advocacy skills to obtain successful results in the full range of personal injury cases, such as:</p>
  <a class="btn btn-gold" style="left:79px;top:981px;width:154px;height:46px">View More</a>

  <div class="service" style="left:454px;top:765px">
    <svg width="52" height="52" viewBox="0 0 52 52"><circle cx="26" cy="26" r="20" fill="none" stroke="#f0a93a" stroke-width="3"/><path d="M14 40h24" stroke="#f0a93a" stroke-width="3"/></svg>
    Slip and Fall
  </div>
  <div class="service" style="left:806px;top:765px">
    <svg width="80" height="52" viewBox="0 0 80 52"><rect x="6" y="20" width="56" height="18" rx="6" fill="none" stroke="#f0a93a" stroke-width="3"/><circle cx="18" cy="40" r="6" fill="#f0a93a"/><circle cx="50" cy="40" r="6" fill="#f0a93a"/></svg>
    Auto Accident
  </div>
  <div class="service" style="left:454px;top:885px">
    <svg width="52" height="56" viewBox="0 0 52 56"><circle cx="26" cy="18" r="11" fill="none" stroke="#f0a93a" stroke-width="3"/><path d="M8 52c0-12 8-18 18-18s18 6 18 18" fill="none" stroke="#f0a93a" stroke-width="3"/></svg>
    Construction Injuries
  </div>
  <div class="service" style="left:806px;top:885px">
    <svg width="52" height="56" viewBox="0 0 52 56"><rect x="12" y="6" width="28" height="26" rx="12" fill="none" stroke="#f0a93a" stroke-width="3"/><path d="M8 52c0-12 8-18 18-18s18 6 18 18" fill="none" stroke="#f0a93a" stroke-width="3"/></svg>
    Medical Malpractice
  </div>
</section>

<section class="abs about">
  <svg class="abs" style="left:0;top:0" width="360" height="442" viewBox="0 0 360 442" aria-hidden="true">
    <circle cx="250" cy="70" r="70" fill="#f7e3c4"/>
    <circle cx="150" cy="170" r="160" fill="#f8e7cc"/>
  </svg>
  <div class="about-photo" role="img" aria-label="Photo of a team of lawyers in suits standing together in an office"></div>
  <div class="accent" style="left:1065px;top:46px"></div>
  <h2 class="section-title" style="right:79px;top:57px">About Us</h2>
  <p class="copy" style="right:79px;top:115px;width:630px;text-align:right">Martin K. Vantholm has successfully handled death and serious personal injury cases involving automobiles and tractor trailers, injuries caused by toxic products, pipeline explosion cases, slip and fall cases involving commercial businesses, and cases against insurance companies.</p>
  <p class="copy" style="right:79px;top:226px;width:630px;text-align:right">Mr. Vantholm is an experienced former insurance defense attorney who fully exploits his insider's knowledge when dealing with insurance companies.</p>
  <a class="btn btn-gold" style="left:967px;top:313px;width:156px;height:43px">View More</a>
</section>

<section class="abs consult">
  <div class="consult-title">GET A FREE<br>CONSULT</div>
  <div class="abs" style="left:329px;top:20px;width:4px;height:95px;background:#2a2a2a"></div>
  <p class="abs" style="left:402px;top:54px;font-size:21px;color:#2a2a2a">We Love help you When Bad things are happen.</p>
  <a class="btn btn-dark" style="left:962px;top:46px;width:159px;height:45px">Get a Quote</a>
</section>

<section class="news">
  <div class="accent" style="left:79px;top:1705px"></div>
  <h2 class="section-title" style="left:79px;top:1714px">Our Recent News</h2>
  <p class="copy" style="left:79px;top:1777px;width:320px">Lorem Ipsum is simply dummy text of the printing and typesetting industry. Lorem Ipsum has been the industry's standard dummy text ever since the 1500s.Lorem Ipsum is simply dummy text of the printing and typesetting industry.</p>
  <a class="btn btn-gold" style="left:79px;top:1944px;width:154px;height:46px">View More</a>

  <article>
    <div class="card-img" style="left:454px;top:1712px" role="img" aria-label="Photo of a consultation meeting in a bright office"></div>
    <div class="date" style="left:450px;top:1720px">28<small>Dec</small></div>
    <h3 class="card-title" style="left:454px;top:1880px">Consulting News Heading Here</h3>
    <div class="card-meta" style="left:454px;top:1912px"><span>Posted By MD,Company Name.</span><span style="margin-left:auto">&#9679; 05</span><span>&#9825; 05</span></div>
    <p class="card-text" style="left:454px;top:1944px">Lorem Ipsum is dummy text.Lorem Ipsum is dummy text.Lorem Ipsum...</p>
    <a class="read-more" style="left:650px;top:1985px">READ MORE <svg width="22" height="22" viewBox="0 0 22 22"><circle cx="11" cy="11" r="9" fill="none" stroke="#e9ad3b" stroke-width="2"/><path d="M7 11h8M12 7l4 4-4 4" stroke="#e9ad3b" stroke-width="2" fill="none"/></svg></a>
  </article>

  <article>
    <div class="card-img" style="left:812px;top:1712px" role="img" aria-label="Photo of an attorney advising a client at a desk"></div>
    <div class="date" style="left:808px;top:1720px">28<small>Dec</small></div>
    <h3 class="card-title" style="left:812px;top:1880px">Consulting News Heading Here</h3>
    <div class="card-meta" style="left:812px;top:1912px"><span>Posted By MD,Company Name.</span><span style="margin-left:auto">&#9679; 05</span><span>&#9825; 05</span></div>
    <p class="card-text" style="left:812px;top:1944px">Lorem Ipsum is dummy text.Lorem Ipsum is dummy text.Lorem Ipsum...</p>
    <a class="read-more" style="left:1008px;top:1985px">READ MORE <svg width="22" height="22" viewBox="0 0 22 22"><circle cx="11" cy="11" r="9" fill="none" stroke="#e9ad3b" stroke-width="2"/><path d="M7 11h8M12 7l4 4-4 4" stroke="#e9ad3b" stroke-width="2" fill="none"/></svg></a>
  </article>
</section>

<section class="abs callback">
  <div class="field" style="top:80px">Name</div>
  <div class="field" style="top:142px">Email Id</div>
  <div class="field" style="top:205px">Contact No</div>
  <div class="message">Message...</div>
  <a class="btn btn-dark" style="left:421px;top:192px;width:166px;height:46px;text-transform:none">SUBMIT NOW</a>
  <div class="accent" style="left:1065px;top:46px;background:#2a2a2a"></div>
  <h2 class="section-title" style="right:79px;top:58px">Request A Call Back</h2>
  <p class="copy" style="right:79px;top:117px;width:330px;text-align:right;color:#4a3a18">Lorem Ipsum is simply dummy text of the printing and typesetting industry. Lorem Ipsum has been the industry's standard dummy text ever since the 1500s.</p>
</section>

<section class="clients">
  <div class="accent" style="left:79px;top:2402px"></div>
  <h2 class="section-title" style="left:79px;top:2410px">Our Happy Clients</h2>

  <div class="quote" style="left:79px;top:2470px">
    <svg width="40" height="30" viewBox="0 0 40 30" style="position:absolute;left:0;top:0"><path d="M0 30V14C0 6 4 1 12 0v6c-4 1-5 4-5 8h5v16zM22 30V14c0-8 4-13 12-14v6c-4 1-5 4-5 8h5v16z" fill="#ddd"/></svg>
    <p class="text" style="text-indent:46px">"Lorem Ipsum is simply dummy text of the printing and typesetting industry. Lorem Ipsum has been the industry's standard dummy text ever since the 1500s.Lorem Ipsum is simply dummy text."</p>
    <div class="avatar" role="img" aria-label="Client portrait photo"></div>
    <div class="who">- Client's Name</div>
    <div class="role">CEO Of Company name</div>
  </div>

  <div class="quote" style="left:444px;top:2470px">
    <svg width="40" height="30" viewBox="0 0 40 30" style="position:absolute;left:0;top:0"><path d="M0 30V14C0 6 4 1 12 0v6c-4 1-5 4-5 8h5v16zM22 30V14c0-8 4-13 12-14v6c-4 1-5 4-5 8h5v16z" fill="#ddd"/></svg>
    <p class="text" style="text-indent:46px">"Lorem Ipsum is simply dummy text of the printing and typesetting industry. Lorem Ipsum has been the industry's standard dummy text ever since the 1500s.Lorem Ipsum is simply dummy text."</p>
    <div class="avatar" role="img" aria-label="Client portrait photo" style="background:linear-gradient(180deg,#e8c69a,#b07a48)"></div>
    <div class="who">- Client's Name</div>
    <div class="role">CEO Of Company name</div>
  </div>

  <div class="quote" style="left:812px;top:2470px">
    <svg width="40" height="30" viewBox="0 0 40 30" style="position:absolute;left:0;top:0"><path d="M0 30V14C0 6 4 1 12 0v6c-4 1-5 4-5 8h5v16zM22 30V14c0-8 4-13 12-14v6c-4 1-5 4-5 8h5v16z" fill="#ddd"/></svg>
    <p class="text" style="text-indent:46px">"Lorem Ipsum is simply dummy text of the printing and typesetting industry. Lorem Ipsum has been the industry's standard dummy text ever since the 1500s.Lorem Ipsum is simply dummy text."</p>
    <div class="avatar" role="img" aria-label="Client portrait photo"></div>
    <div class="who">- Client's Name</div>
    <div class="role">CEO Of Company name</div>
  </div>
</section>

<footer class="abs footer">
  <div class="abs" style="left:77px;top:52px;width:131px;height:146px;border:2px solid var(--gold-deep);background:linear-gradient(180deg,#6b5a4e,#2a2422)" role="img" aria-label="Portrait photo of Martin K. Vantholm"></div>
  <div class="abs" style="left:86px;top:212px;width:70px;height:38px;background:#555;border-radius:4px" role="img" aria-label="Award badge"></div>
  <h4 style="left:231px;top:60px">Martin K. Vantholm</h4>
  <div class="abs" style="left:238px;top:104px;display:flex;gap:22px">
    <span style="width:14px;height:14px;border-radius:50%;background:#ddd"></span>
    <span style="width:14px;height:14px;border-radius:50%;background:#ddd"></span>
    <span style="width:14px;height:14px;border-radius:50%;background:#ddd"></span>
    <span style="width:14px;height:14px;border-radius:50%;background:#ddd"></span>
  </div>
  <p class="abs" style="left:231px;top:146px;font-size:16px;line-height:22px">2006 &amp; 2007 Pennsylvania<br>Rising Star,</p>
  <p class="abs" style="left:231px;top:190px;font-family:var(--serif);font-size:20px;color:var(--gold)">Top Trial Counsel</p>

  <h4 style="left:525px;top:60px">Links</h4>
  <ul class="links">
    <li>Home</li><li>Slip and Fall</li><li>Auto Accident</li><li>Construction Injuries</li><li>Medical Malpractice</li><li>Results</li><li>About Us</li><li>Contcat Us</li>
  </ul>

  <h4 style="left:812px;top:60px">Get in touch</h4>
  <div class="contact-row" style="top:98px">
    <svg width="18" height="22" viewBox="0 0 18 22"><path d="M9 0v22M2 4h14l2 2-2 2H2zM2 11h14l-2 2 2 2H2z" fill="#ddd" stroke="#ddd"/></svg>
    <span>Martin K. Vantholm,<br>2400 Harbor Ave #310,<br>Riverton, PA, 19000</span>
  </div>
  <div class="contact-row" style="top:192px">
    <svg width="18" height="18" viewBox="0 0 16 16"><path d="M3 1l3 3-2 2c1 2 3 4 5 5l2-2 3 3-2 3C7 15 1 9 1 3z" fill="#ddd"/></svg>
    <span>(555) 010-2290</span>
  </div>
  <div class="contact-row" style="top:240px">
    <svg width="20" height="16" viewBox="0 0 20 16"><rect x="1" y="1" width="18" height="14" fill="none" stroke="#ddd" stroke-width="2"/><path d="M1 1l9 7 9-7" stroke="#ddd" stroke-width="2" fill="none"/></svg>
    <span>martin@vantholmlegal.example</span>
  </div>

  <div class="abs" style="left:79px;top:333px;width:1042px;height:1px;background:#8a6a2a"></div>
  <p class="copyright">&copy; <b>VANTHOLM INJURY LAWGROUP</b> , <span>Martin K. Vantholm</span> - 2016 All Right Reserved</p>
</footer>

</body>
</html>
```